Litigation Support Company Needing new Simple Web Design

I need to re-design a self done wix hosted website for a small yet nation-wide litigation support consulting firm. I built mine at www.brieflantern-hub.com myself when I launched but it is very hard on the eyes and needs refreshing/updates. Thanks for taking a look!

Target Market(s)

Law firms and technology experts in the litigation support field.

Number of Pages Required

4 page

Font styles to use
Serif

Colors
f78f20
faa54b
fac994

Requirements
Must have
• Blog, About Us, Services Pages, Crisper Graphics etc.

```html
<!DOCTYPE html>
<html lang="en">
<head>
<meta charset="utf-8">
<title>brieflantern – Litigation Support</title>
<link rel="stylesheet" href="https://fonts.googleapis.com/css2?family=Poppins:wght@300;400;500;600&family=Open+Sans:wght@400;600&display=swap">
<style>
:root{
  --orange:#f78f20;
  --orange-mid:#faa54b;
  --orange-soft:#fac994;
  --ink:#333333;
  --muted:#777777;
  --dark:#2b2b2b;
  --darker:#222222;
  --line:#e4e4e4;
  --white:#ffffff;
}
*{box-sizing:border-box;margin:0;padding:0}
html,body{width:1200px;height:2584px;overflow:hidden}
body{font-family:"Open Sans",Arial,sans-serif;color:var(--ink);background:var(--white);position:relative}
h1,h2,h3,h4,.nav,.btn{font-family:"Poppins",Arial,sans-serif}

.site-header{height:60px;display:flex;align-items:center;justify-content:space-between;padding:0 80px 0 44px;background:var(--white)}
.brand{display:flex;align-items:center;gap:8px;font-family:"Poppins",sans-serif;font-weight:600;font-size:26px;color:var(--ink)}
.brand-dot{width:16px;height:16px;border-radius:50%;background:var(--orange)}
.nav{display:flex;gap:34px;font-size:14px}
.nav a{color:var(--ink);text-decoration:none}
.nav a.active{color:var(--orange)}

.hero{position:absolute;top:60px;left:0;width:1200px;height:560px;background:linear-gradient(180deg,#5d5a56 0%,#6f6a64 45%,#4a4743 100%);text-align:center;color:var(--white)}
.hero-title{margin-top:248px;font-size:58px;font-weight:500;letter-spacing:1px}
.hero-sub{width:560px;margin:10px auto 0;font-size:15px;line-height:26px}
.arrow{position:absolute;top:348px;width:34px;height:34px;border-radius:50%;background:rgba(0,0,0,.55);display:flex;align-items:center;justify-content:center}
.arrow.left{left:36px}.arrow.right{right:36px}

.feature-cards{position:absolute;top:592px;left:88px;width:1024px;height:328px;display:flex}
.card{flex:1;padding:50px 50px 0;color:var(--white)}
.card.managed{background:var(--orange)}
.card.review{background:#3a3a3a;padding-left:90px}
.card h3{font-size:20px;font-weight:500;margin-bottom:20px}
.card p{font-size:13px;line-height:22px;opacity:.95}
.btn{display:inline-block;font-size:14px;padding:10px 22px;text-decoration:none}
.card .btn{margin-top:30px;border:1px solid var(--white);color:var(--white)}
.card.review .btn{background:#222;border-color:#222}
.card-badge{position:absolute;left:462px;top:114px;width:100px;height:100px;border-radius:50%;background:var(--white);border:6px solid var(--orange)}

.about{position:absolute;top:950px;left:0;width:1200px;text-align:center}
.section-title{font-size:34px;font-weight:400;color:var(--ink)}
.rule{width:64px;height:2px;background:var(--orange);margin:14px auto 0}
.about p{width:680px;margin:36px auto 0;font-size:13px;line-height:24px;color:var(--muted)}
.btn.solid{background:var(--orange);color:var(--white);margin-top:34px;padding:12px 34px}

.band{position:absolute;top:1260px;left:0;width:1200px;height:260px;background:linear-gradient(90deg,#6a625a 0%,#8a7f74 50%,#5c554f 100%);text-align:center;color:var(--white)}
.band h2{margin-top:66px;font-size:30px;font-weight:500;letter-spacing:1px}
.band h4{font-size:26px;font-weight:400;margin-top:4px}
.band .btn.solid{margin-top:26px}

.blog{position:absolute;top:1640px;left:0;width:1200px;text-align:center}
.blog-sub{font-size:13px;color:var(--muted);margin-top:26px}
.posts{display:flex;gap:46px;justify-content:center;margin-top:44px}
.post{width:308px;height:460px;border:1px solid var(--line);text-align:center}
.post-photo{height:210px}
.post h4{font-size:14px;font-weight:500;margin-top:30px;letter-spacing:.5px}
.post .date{font-size:13px;color:var(--orange);margin-top:12px}
.post p{font-size:12.5px;line-height:22px;color:var(--muted);padding:14px 28px 0}

.site-footer{position:absolute;top:2260px;left:0;width:1200px;height:324px;background:var(--dark);color:var(--white)}
.social{display:flex;gap:18px;justify-content:center;margin-top:44px}
.social span{width:44px;height:44px;border:1px solid #777;border-radius:50%;display:block}
.contacts{display:flex;justify-content:space-between;padding:0 150px;margin-top:56px}
.contact{display:flex;gap:16px;align-items:flex-start;width:260px}
.contact h4{font-size:18px;font-weight:400}
.contact p{font-size:12px;color:#bbb;margin-top:6px;line-height:18px}
.copy{position:absolute;bottom:0;width:100%;height:70px;line-height:70px;text-align:center;font-size:12px;color:#aaa;background:var(--darker)}
</style>
</head>
<body>

<header class="site-header">
  <div class="brand"><span class="brand-dot"></span>brieflantern</div>
  <nav class="nav">
    <a class="active" href="#">Home</a><a href="#">About Us</a><a href="#">Services</a><a href="#">Blog</a><a href="#">Contact us</a>
  </nav>
</header>

<section class="hero" role="img" aria-label="Photo of a legal team meeting around a table">
  <h1 class="hero-title">brieflantern</h1>
  <p class="hero-sub">Licensed knowledge and methods focused on the absolutely most important steps to succeed in any eDiscovery review project</p>
  <span class="arrow left"><svg width="12" height="12" viewBox="0 0 12 12"><path d="M8 1 3 6l5 5" fill="none" stroke="#fff" stroke-width="2"/></svg></span>
  <span class="arrow right"><svg width="12" height="12" viewBox="0 0 12 12"><path d="M4 1l5 5-5 5" fill="none" stroke="#fff" stroke-width="2"/></svg></span>
</section>

<section class="feature-cards">
  <article class="card managed">
    <h3>E-Discovery Managed Services</h3>
    <p>E-Discovery case tasks managed by our experienced team, from early planning and data collection through review, production and final reporting for counsel.</p>
    <a class="btn" href="#">Learn More</a>
  </article>
  <article class="card review">
    <h3>Discovery Review Consultation</h3>
    <p>Attorneys gain clear guidance from a team with years of experience building defensible review plans, so every project meets budget and deadline.</p>
    <a class="btn" href="#">Learn More</a>
  </article>
  <span class="card-badge"></span>
</section>

<section class="about">
  <h2 class="section-title">About brieflantern</h2>
  <div class="rule"></div>
  <p>We believe proper application of technology can make or break the discovery process of small and large matters alike. Our review projects are run by seasoned consultants who keep each step transparent and focused on results for the client.</p>
  <a class="btn solid" href="#">Read More</a>
</section>

<section class="band" role="img" aria-label="Photo of two colleagues shaking hands">
  <h2>SED UT PERSPICIATIS UNDE OMNIS ISTE</h2>
  <h4>error sit voluptatem accusantium doloremque laudantium</h4>
  <a class="btn solid" href="#">Read More</a>
</section>

<section class="blog">
  <h2 class="section-title">Latest Blog</h2>
  <div class="rule"></div>
  <p class="blog-sub">Short notes and field tips from our consultants on modern discovery review work</p>
  <div class="posts">
    <article class="post">
      <div class="post-photo" role="img" aria-label="Photo of a laptop on a desk" style="background:linear-gradient(135deg,#b9b2a8,#7d776f)"></div>
      <h4>IDENTIFYING KEY FACTS</h4>
      <div class="date">June 20, 2016</div>
      <p>Finding the facts that matter early shapes every later step of a review and keeps costs under control.</p>
    </article>
    <article class="post">
      <div class="post-photo" role="img" aria-label="Photo of a team working together at a table" style="background:linear-gradient(135deg,#9aa6b4,#5f6670)"></div>
      <h4>NEVER STOP DISCOVERING</h4>
      <div class="date">June 20, 2016</div>
      <p>Learning never stops in this field; new tools and rules arrive each year and we study them closely.</p>
    </article>
    <article class="post">
      <div class="post-photo" role="img" aria-label="Photo of documents and charts on a desk" style="background:linear-gradient(135deg,#c9a77c,#7a6650)"></div>
      <h4>THE NATIVES ARE RESTLESS</h4>
      <div class="date">June 20, 2016</div>
      <p>What does proportional discovery really mean for a small team? We walk through the practical answer here.</p>
    </article>
  </div>
</section>

<footer class="site-footer">
  <div class="social"><span></span><span></span><span></span><span></span><span></span><span></span></div>
  <div class="contacts">
    <div class="contact">
      <svg width="28" height="34" viewBox="0 0 28 34"><path d="M14 2a10 10 0 0 0-10 10c0 8 10 20 10 20s10-12 10-20A10 10 0 0 0 14 2z" fill="none" stroke="#fff" stroke-width="2"/><circle cx="14" cy="12" r="4" fill="#fff"/></svg>
      <div><h4>Address :</h4><p>418 Alder Court, Suite 12<br>Denver CO 80204</p></div>
    </div>
    <div class="contact">
      <svg width="32" height="24" viewBox="0 0 32 24"><rect x="1" y="1" width="30" height="22" fill="none" stroke="#fff" stroke-width="2"/><path d="M1 1l15 12L31 1" fill="none" stroke="#fff" stroke-width="2"/></svg>
      <div><h4>Email</h4><p>hello@brieflantern-hub.com</p></div>
    </div>
    <div class="contact">
      <svg width="26" height="32" viewBox="0 0 26 32"><rect x="3" y="1" width="20" height="30" rx="3" fill="none" stroke="#fff" stroke-width="2"/><circle cx="13" cy="26" r="1.8" fill="#fff"/></svg>
      <div><h4>Phone</h4><p>Mobile : (555) 210-4837</p></div>
    </div>
  </div>
  <div class="copy">© Copyright 2016 brieflantern All Rights Reserved</div>
</footer>

</body>
</html>
```